Brightpath Medical Exercise, LLC specializes in post rehab medical exercise for clients who have been discharged from physical therapy and/or other medical services and are in need of continued cardiovascular, strength, flexibility, endurance training and management of their medical conditions. We strive to bridge the gap between healthcare and fitness by staying in communication with the referring physician and /or physical therapist with updated progress notes to follow each clients progression, making sure each client is appropriate for exercise and identifying any red flags throughout the initial assessment and screening of the client, and referring those clients back to the physician and/or therapist when necessary.
Colors
Designer to choose colors to be used in the design.
Requirements
Must have
- Pictures of a trainer working with a client one on one during exercise, and group exercise
Nice to have
- Pictures that portray the bridge between healthcare and fitness
Should not have
- Cursive writing

```html
<!DOCTYPE html>
<html lang="en">
<head>
<meta charset="utf-8">
<title>Brightpath Medical Exercise, LLC – Conditions Rack Card</title>
<link href="https://fonts.googleapis.com/css2?family=Raleway:wght@400;500;700;800&display=swap" rel="stylesheet">
<style>
  :root {
    --coral: #f15a50;
    --ink: #222222;
    --text: #333333;
    --paper: #ffffff;
    --backdrop: #ececec;
    --mist-a: #f6efed;
    --mist-b: #eae6e4;
  }
  * { box-sizing: border-box; margin: 0; padding: 0; }
  html, body { width: 688px; height: 1200px; overflow: hidden; }
  body {
    background: var(--backdrop);
    font-family: "Raleway", sans-serif;
    color: var(--text);
  }
  .rack-card {
    position: relative;
    width: 576px;
    height: 1200px;
    margin: 0 auto;
    background: var(--paper);
    overflow: hidden;
  }
  .top-band {
    position: absolute; top: 0; left: 0; right: 0; height: 25px;
    background: var(--coral);
  }
  .hero-photo {
    position: absolute; top: 25px; left: 0; right: 0; height: 1000px;
    background: linear-gradient(160deg, var(--mist-a) 0%, #fbf8f7 45%, var(--mist-b) 100%);
    opacity: .8;
  }
  .shapes { position: absolute; inset: 0; }
  .headline {
    position: absolute; top: 62px; left: 58px;
    line-height: 1;
  }
  .headline .lead {
    display: block; font-size: 26px; font-weight: 400; color: var(--ink);
    letter-spacing: .3px;
  }
  .headline .accent {
    display: block; font-size: 32px; font-weight: 800; color: var(--coral);
    margin-top: 8px; line-height: 40px;
  }
  .conditions {
    position: absolute; top: 198px; list-style: none;
    font-size: 17px; line-height: 19px; white-space: nowrap;
  }
  .conditions.col-left { left: 58px; }
  .conditions.col-right { left: 313px; }
  .conditions li {
    position: relative; padding-left: 25px; margin-bottom: 11px;
  }
  .conditions li::before {
    content: ""; position: absolute; left: 0; top: 5px;
    width: 9px; height: 9px; background: var(--coral);
  }
  .quote {
    position: absolute; top: 745px; left: 0; right: 0;
    text-align: center; padding-left: 12px;
  }
  .quote-text {
    font-size: 23px; font-weight: 700; color: var(--ink); line-height: 28px;
  }
  .quote-author {
    margin-top: 14px; font-size: 24px; font-weight: 400; color: var(--ink);
  }
  .quote-mark {
    position: absolute; font-weight: 800; font-size: 84px; color: var(--ink);
    line-height: 1; font-family: "Raleway", sans-serif;
  }
</style>
</head>
<body>
<main class="rack-card">
  <div class="hero-photo" role="img" aria-label="Faded photo of a trainer guiding a client through a shoulder exercise"></div>
  <div class="top-band"></div>

  <svg class="shapes" width="576" height="1200" viewBox="0 0 576 1200">
    <defs>
      <linearGradient id="deckPhoto" x1="0" y1="0" x2="0" y2="1">
        <stop offset="0" stop-color="#2f3b2c"/>
        <stop offset="0.45" stop-color="#4a4a3e"/>
        <stop offset="0.6" stop-color="#a88e72"/>
        <stop offset="1" stop-color="#c9b196"/>
      </linearGradient>
    </defs>
    <circle cx="92" cy="716" r="34" fill="var(--coral)"/>
    <line x1="120" y1="716" x2="474" y2="716" stroke="var(--coral)" stroke-width="3"/>
    <line x1="101" y1="899" x2="450" y2="899" stroke="var(--coral)" stroke-width="3"/>
    <circle cx="474" cy="899" r="34" fill="var(--coral)"/>
    <path d="M0,1058 Q290,860 576,1148 L576,1200 L0,1200 Z" fill="url(#deckPhoto)" role="img" aria-label="Photo of a water bottle and two blue dumbbells on a wooden deck"/>
    <path d="M0,1058 Q290,860 576,1148" fill="none" stroke="var(--coral)" stroke-width="8"/>
  </svg>

  <span class="quote-mark" style="left:66px;top:690px;">“</span>
  <span class="quote-mark" style="left:447px;top:872px;">”</span>

  <h1 class="headline">
    <span class="lead">WE OFFER MANAGEMENT</span>
    <span class="accent">OF THE FOLLOWING<br>CONDITIONS AND MORE:</span>
  </h1>

  <ul class="conditions col-left">
    <li>Diabetes AC</li>
    <li>Hypertension</li>
    <li>ACL Rupture</li>
    <li>Ankle Fracture</li>
    <li>Bicipital Tendonitis</li>
    <li>Total Hip<br>Replacement</li>
    <li>Total Knee<br>Replacement</li>
    <li>Spinal Stenosis</li>
    <li>Multiple Sclerosis</li>
    <li>Shoulder Dislocation</li>
    <li>Scoliosis</li>
    <li>Osteoporosis</li>
    <li>Osteoarthritis</li>
    <li>Cervical disc herniation</li>
  </ul>

  <ul class="conditions col-right">
    <li>Joint Separation</li>
    <li>Fibromyalgia</li>
    <li>Spondylothesis</li>
    <li>Parkinson’s Disease</li>
    <li>Tibial Plateau Fracture</li>
    <li>Tennis Elbow/Golfer’s<br>Elbow</li>
    <li>Carpal Tunnel Syndrome</li>
    <li>Total Shoulder<br>Replacement</li>
    <li>Bicipital Tendonitis</li>
    <li style="letter-spacing:-.4px;">Patello-Femoral Syndrome</li>
    <li>Rotator Cuff Syndrome</li>
    <li>Cervical Strain</li>
    <li>Impingement Syndrome</li>
    <li>Laminectomy</li>
  </ul>

  <blockquote class="quote">
    <p class="quote-text">Exercise is the key<br>to long-term management<br>of most medical conditions</p>
    <p class="quote-author">~ Daniel R Hayes, PhD, PT</p>
  </blockquote>
</main>
</body>
</html>
```